Company Postage Label

Design a postage label that measures: 16cm long x 9cm high with a sticky back to stick on boxes. Similar to the attached from Talvora Carriers.

Industry/Entity Type

Motorcycle Part

Colors

Designer to choose colors to be used in the design.

Requirements
Must have
• Company logo and address

```html
<!DOCTYPE html>
<html lang="en">
<head>
<meta charset="utf-8">
<title>Postage Label – Ridgeline Exhaust Works</title>
<link href="https://fonts.googleapis.com/css2?family=PT+Sans:wght@400;700&display=swap" rel="stylesheet">
<style>
  :root {
    --canvas: #ece9e4;
    --paper: #ffffff;
    --ink: #111111;
    --brand-red: #c8171e;
  }
  html, body {
    margin: 0;
    padding: 0;
    width: 1200px;
    height: 795px;
    overflow: hidden;
    background: var(--canvas);
  }
  .label {
    position: absolute;
    left: 80px;
    top: 105px;
    width: 1040px;
    height: 585px;
    font-family: "PT Sans", sans-serif;
  }
  .label text { font-family: "PT Sans", sans-serif; fill: var(--ink); }
  .label .frame { fill: var(--paper); stroke: var(--ink); stroke-width: 12; }
  .label .cut-line { fill: none; stroke: var(--ink); stroke-width: 2.5; stroke-dasharray: 8 5; }
  .label .divider { stroke: var(--ink); stroke-width: 6; }
  .label .write-line { stroke: var(--ink); stroke-width: 1.6; }
  .label .postcode-box { fill: none; stroke: var(--ink); stroke-width: 1.6; }
  .label .scissors { fill: none; stroke: var(--ink); stroke-width: 2; }
  .label .carrier-badge { fill: var(--ink); }
  .label .carrier-name { font-weight: 700; font-size: 24px; fill: var(--paper); }
  .label .client-name { font-weight: 700; font-size: 22px; fill: var(--brand-red); }
  .label .stamp-note { font-size: 17px; }
  .label .field-label { font-size: 13px; }
  .label .print-code { font-size: 13px; }
</style>
</head>
<body>
<svg class="label" viewBox="0 0 1040 585" xmlns="http://www.w3.org/2000/svg">
  <defs>
    <g id="scissors-icon" class="scissors">
      <circle cx="-6" cy="-5" r="3.5"/>
      <circle cx="-6" cy="5" r="3.5"/>
      <line x1="-3" y1="-3" x2="9" y2="5"/>
      <line x1="-3" y1="3" x2="9" y2="-5"/>
    </g>
  </defs>

  <!-- card -->
  <rect class="frame" x="6" y="6" width="1028" height="573"/>
  <rect class="cut-line" x="24" y="24" width="992" height="537"/>

  <!-- cut marks -->
  <rect x="672" y="14" width="36" height="20" fill="var(--paper)"/>
  <use href="#scissors-icon" transform="translate(690 24)"/>
  <rect x="1006" y="348" width="20" height="36" fill="var(--paper)"/>
  <use href="#scissors-icon" transform="translate(1016 366) rotate(90)"/>
  <rect x="500" y="551" width="36" height="20" fill="var(--paper)"/>
  <use href="#scissors-icon" transform="translate(518 561)"/>
  <rect x="14" y="130" width="20" height="36" fill="var(--paper)"/>
  <use href="#scissors-icon" transform="translate(24 148) rotate(90)"/>

  <!-- sender panel -->
  <line class="divider" x1="236" y1="6" x2="236" y2="579"/>
  <g class="sender-lines">
    <line class="write-line" x1="85" y1="50" x2="85" y2="540"/>
    <line class="write-line" x1="120" y1="50" x2="120" y2="540"/>
    <line class="write-line" x1="155" y1="50" x2="155" y2="540"/>
    <line class="write-line" x1="190" y1="50" x2="190" y2="540"/>
  </g>
  <text class="field-label" transform="translate(62 540) rotate(-90)">FROM</text>

  <!-- carrier badge -->
  <rect class="carrier-badge" x="270" y="48" width="210" height="36" rx="18"/>
  <text class="carrier-name" x="375" y="74" text-anchor="middle">Talvora Carriers</text>

  <!-- client name -->
  <text class="client-name" x="640" y="100" text-anchor="middle">Ridgeline Exhaust Works</text>

  <text class="stamp-note" x="990" y="74" text-anchor="end">Please Affix Stamps</text>
  <text class="stamp-note" x="990" y="95" text-anchor="end">Before Mailing</text>

  <!-- recipient -->
  <text class="field-label" x="300" y="152">To</text>
  <g class="recipient-lines">
    <line class="write-line" x1="318" y1="160" x2="990" y2="160"/>
    <line class="write-line" x1="300" y1="205" x2="990" y2="205"/>
    <line class="write-line" x1="300" y1="250" x2="990" y2="250"/>
    <line class="write-line" x1="300" y1="295" x2="990" y2="295"/>
    <line class="write-line" x1="300" y1="340" x2="990" y2="340"/>
  </g>

  <!-- postcode boxes -->
  <g class="postcode">
    <rect class="postcode-box" x="312" y="368" width="86" height="54"/>
    <rect class="postcode-box" x="398" y="368" width="86" height="54"/>
    <rect class="postcode-box" x="484" y="368" width="86" height="54"/>
    <rect class="postcode-box" x="570" y="368" width="86" height="54"/>
    <rect class="postcode-box" x="656" y="368" width="86" height="54"/>
    <rect class="postcode-box" x="742" y="368" width="86" height="54"/>
    <rect class="postcode-box" x="828" y="368" width="86" height="54"/>
  </g>

  <text class="print-code" x="1000" y="545" text-anchor="end">4172608 (RX42) Mar'21</text>
</svg>
</body>
</html>
```